Business cards Dör Kornhüüs GmbH & Co.KG

We need a uniform business card design template for our employees.
A template should be created to have the same design for all business cards.

Contact Information for Business Card

Firma und Firmierung, Name, Funktion in Unternehmen, Anschrift, Tel. Handynummer, Emailadresse, Internetseite

Colors

Designer to choose colors to be used in the design.

Requirements
Must have
• Our company logo must be on it

```html
<!DOCTYPE html>
<html lang="de">
<head>
<meta charset="utf-8">
<title>Dör Kornhüüs – Visitenkarte</title>
<link rel="stylesheet" href="https://fonts.googleapis.com/css2?family=Cormorant+SC:wght@700&family=Montserrat:wght@300&display=swap">
<style>
  :root {
    --card-bg: #19191a;
    --accent-pink: #f0677a;
    --soft-lilac: #c9a3cf;
    --serif: "Cormorant SC", serif;
    --sans: "Montserrat", sans-serif;
  }
  html, body {
    margin: 0;
    padding: 0;
    width: 1200px;
    height: 721px;
    overflow: hidden;
    background: var(--card-bg);
  }
  .business-card {
    position: relative;
    width: 1200px;
    height: 721px;
    background: var(--card-bg);
    color: var(--soft-lilac);
    font-family: var(--sans);
    font-weight: 300;
  }
  .brand-name {
    position: absolute;
    left: 170px;
    top: 168px;
    margin: 0;
    font-family: var(--serif);
    font-weight: 700;
    font-size: 58px;
    line-height: 1;
    color: var(--accent-pink);
    letter-spacing: 1px;
  }
  .contact-block {
    position: absolute;
    left: 607px;
    top: 190px;
  }
  .person-name {
    margin: 0;
    font-family: var(--serif);
    font-weight: 700;
    font-size: 42px;
    line-height: 1;
    letter-spacing: 1.5px;
    color: var(--accent-pink);
  }
  .person-role {
    margin: 4px 0 0;
    font-size: 28px;
    line-height: 1.1;
  }
  .contact-list {
    list-style: none;
    margin: 34px 0 0;
    padding: 0;
  }
  .contact-item {
    display: flex;
    align-items: center;
    gap: 14px;
    font-size: 29px;
    line-height: 38px;
  }
  .contact-icon {
    width: 27px;
    height: 27px;
    flex: none;
    stroke: var(--accent-pink);
    fill: none;
    stroke-width: 2;
  }
  .postal-address {
    margin: 40px 0 0;
    font-style: normal;
    font-size: 29px;
    line-height: 37px;
  }
  .legal-form {
    margin: 0;
    font-family: var(--serif);
    font-weight: 700;
    font-size: 33px;
    line-height: 38px;
    color: var(--accent-pink);
  }
  .accent-dash {
    position: absolute;
    left: 607px;
    top: 616px;
    width: 26px;
    height: 5px;
    background: var(--accent-pink);
  }
</style>
</head>
<body>
  <main class="business-card">
    <p class="brand-name">Dör Kornhüüs</p>

    <section class="contact-block">
      <h1 class="person-name">HENRIK ALBERS</h1>
      <p class="person-role">Sales Manager</p>

      <ul class="contact-list">
        <li class="contact-item">
          <svg class="contact-icon" viewBox="0 0 24 24" aria-hidden="true">
            <path d="M6.5 3h3l1.5 4.5-2 1.5a11 11 0 0 0 6 6l1.5-2 4.5 1.5v3a2 2 0 0 1-2 2A17 17 0 0 1 4.5 5a2 2 0 0 1 2-2z"/>
          </svg>
          555-318-2407
        </li>
        <li class="contact-item">
          <svg class="contact-icon" viewBox="0 0 24 24" aria-hidden="true">
            <rect x="2.5" y="5" width="19" height="14" rx="1"/>
            <path d="M2.5 5.5 12 13l9.5-7.5M2.5 18.5l7-6.5M21.5 18.5l-7-6.5"/>
          </svg>
          info@doerkornhuues.com
        </li>
        <li class="contact-item">
          <svg class="contact-icon" viewBox="0 0 24 24" aria-hidden="true">
            <circle cx="12" cy="12" r="9.5"/>
            <path d="M2.5 12h19M12 2.5c3 3 3 16 0 19M12 2.5c-3 3-3 16 0 19M4 7h16M4 17h16"/>
          </svg>
          www.doerkornhuues.com
        </li>
      </ul>

      <address class="postal-address">
        PO Box 248, Harlow Vale<br>
        Qld 4901
      </address>
      <p class="legal-form">GmbH &amp; Co.KG</p>
    </section>

    <div class="accent-dash"></div>
  </main>
</body>
</html>
```